bail bonds business

Need a web design for a Bail Bond company. At Larkmoor Bails, we specialize in getting arrested defendants out of jail. Also, I have all the necessary information already uploaded in the files.

Target Market(s)

Arrested defendants and their families who will post bails on their behalf.

Industry/Entity Type

Business

Coding

Coded - Design and coding required

Number of Pages Required

1 page

```html
<!DOCTYPE html>
<html lang="en">
<head>
<meta charset="utf-8">
<title>Larkmoor Bails Inc</title>
<link href="https://fonts.googleapis.com/css2?family=Open+Sans:wght@400;600;700;800&display=swap" rel="stylesheet">
<style>
:root{
  --red:#c8102e;
  --dark:#2b2320;
  --darker:#1c1614;
  --text:#444;
  --muted:#8a8a8a;
  --light:#f2f2f2;
  --line:#e2e2e2;
  --white:#fff;
  --social-a:#3b5b9a;
  --social-b:#2aa3dc;
  --social-c:#d9472b;
}
*{box-sizing:border-box;margin:0;padding:0}
html,body{width:764px;height:1200px;overflow:hidden}
body{font-family:"Open Sans",Arial,sans-serif;color:var(--text);background:var(--white);font-size:10px}
.container{width:672px;margin:0 auto;position:relative}

/* header */
.site-header{height:90px;background:var(--white);position:relative}
.brand{position:absolute;left:0;top:20px;display:flex;align-items:center;gap:8px}
.brand-mark{width:30px;height:30px;background:var(--red)}
.brand-name{font-weight:800;font-size:15px;color:var(--dark);letter-spacing:.3px;text-transform:uppercase}
.topbar{position:absolute;right:0;top:16px;display:flex;align-items:center;gap:6px}
.topbar-label{font-size:7px;color:var(--muted);letter-spacing:.5px;margin-right:4px}
.social{width:16px;height:16px;border-radius:50%}
.social.a{background:var(--social-a)}.social.b{background:var(--social-b)}.social.c{background:var(--social-c)}
.search{width:74px;height:18px;border:1px solid var(--line);margin-left:8px;position:relative;font-size:7px;color:var(--muted);padding:4px 6px}
.search svg{position:absolute;right:5px;top:4px}
.main-nav{position:absolute;right:0;top:58px;display:flex;gap:2px}
.main-nav a{font-size:7.5px;font-weight:600;color:var(--dark);text-decoration:none;padding:5px 9px;letter-spacing:.3px}
.main-nav a.active{background:var(--red);color:var(--white)}

/* hero */
.hero{height:407px;position:relative;background:linear-gradient(180deg,#4a5868 0%,#2a2f3c 35%,#1a1d2a 60%,#3a2f34 85%,#1d1c24 100%);overflow:hidden}
.hero-photo{position:absolute;inset:0;background:radial-gradient(ellipse at 55% 55%,rgba(255,190,120,.35),transparent 55%),radial-gradient(ellipse at 20% 70%,rgba(120,170,255,.25),transparent 50%)}
.hero-title{position:absolute;left:0;right:0;top:190px;text-align:center;color:var(--white);font-weight:800;font-size:22px;letter-spacing:1.5px;line-height:1.25;text-transform:uppercase}
.hero-arrow{position:absolute;top:190px;width:22px;height:30px;background:var(--red);display:flex;align-items:center;justify-content:center}
.hero-arrow.left{left:0}.hero-arrow.right{right:0}
.hero-dots{position:absolute;bottom:25px;left:0;right:0;display:flex;justify-content:center;gap:6px}
.hero-dots span{width:6px;height:6px;border-radius:50%;background:rgba(255,255,255,.5)}
.hero-dots span.on{background:var(--white)}

/* features */
.features{height:103px;border-bottom:1px solid var(--line)}
.features .container{display:flex;height:100%;align-items:center}
.feature{flex:1;display:flex;align-items:center;gap:14px;padding-left:36px;border-right:1px solid var(--line);height:46px}
.feature:last-child{border-right:none}
.feature p{font-size:9px;color:#555;line-height:1.4;width:110px}

/* offer */
.offer{height:215px;background:var(--light);position:relative}
.section-title{text-align:center;color:var(--red);font-weight:700;font-size:11px;letter-spacing:.6px;padding-top:26px;text-transform:uppercase}
.section-title::after{content:"";display:block;width:150px;height:1px;background:var(--line);margin:6px auto 0}
.cards{display:flex;gap:10px;justify-content:center;margin-top:18px}
.card{width:185px;text-align:center}
.card-img{height:82px}
.card-img.drug{background:linear-gradient(135deg,#e9e3d9,#c9a98a 60%,#b84a2a)}
.card-img.crime{background:linear-gradient(135deg,#d9dde3,#7a8a9c 50%,#b0101e)}
.card-img.dui{background:linear-gradient(135deg,#f0efe9,#c8a05a 55%,#5a3a1c)}
.card h3{color:var(--red);font-size:9.5px;font-weight:600;margin-top:8px}
.card p{font-size:7px;color:var(--muted);margin-top:3px}
.card a{display:block;font-size:6.5px;font-weight:700;color:var(--dark);letter-spacing:.6px;margin-top:7px;text-decoration:none}
.offer-arrow{position:absolute;top:112px;width:16px;height:16px;border-radius:50%;border:1px solid #ccc;display:flex;align-items:center;justify-content:center;background:var(--white)}
.offer-arrow.left{left:44px}.offer-arrow.right{right:44px}

/* services */
.services{height:217px}
.service-list{display:flex;justify-content:center;gap:30px;margin-top:24px}
.service{width:190px;text-align:center}
.service svg{display:block;margin:0 auto}
.service h3{font-size:12px;font-weight:400;color:#333;margin-top:8px}
.service p{font-size:7px;color:var(--muted);line-height:1.5;margin-top:6px;padding:0 14px}

/* footer */
.site-footer{height:140px;background:var(--dark);color:#bdb6b2}
.site-footer .container{display:flex;padding-top:22px;gap:24px}
.footer-col h4{color:var(--white);font-size:8px;font-weight:700;letter-spacing:.5px;margin-bottom:12px;text-transform:uppercase}
.footer-col p{font-size:7px;line-height:1.7}
.contact{width:250px}
.contact-row{display:flex;gap:22px}
.newsletter{width:200px}
.email-field{display:flex;height:22px;background:#3b322e}
.email-field span{flex:1;font-size:7px;padding:6px 8px;color:#9a908b}
.email-field b{width:22px;background:#4a403b;display:flex;align-items:center;justify-content:center}
.follow{flex:1;text-align:right}
.follow .socials{display:flex;gap:6px;justify-content:flex-end}
.bottom-bar{height:28px;background:var(--darker);color:#8e8580;font-size:6.5px}
.bottom-bar .container{display:flex;justify-content:space-between;align-items:center;height:28px}
.bottom-bar nav{display:flex;gap:10px;letter-spacing:.3px}
</style>
</head>
<body>

<header class="site-header">
  <div class="container">
    <div class="brand">
      <span class="brand-mark"></span>
      <span class="brand-name">Larkmoor Bails Inc</span>
    </div>
    <div class="topbar">
      <span class="topbar-label">FOLLOW US ON</span>
      <span class="social a"></span><span class="social b"></span><span class="social c"></span>
      <div class="search">Search
        <svg width="9" height="9" viewBox="0 0 10 10"><circle cx="4" cy="4" r="3" fill="none" stroke="#999" stroke-width="1.3"/><line x1="6.3" y1="6.3" x2="9" y2="9" stroke="#999" stroke-width="1.3"/></svg>
      </div>
    </div>
    <nav class="main-nav">
      <a class="active" href="#">HOME</a>
      <a href="#">ABOUT US</a>
      <a href="#">WHAT WE OFFER</a>
      <a href="#">SERVICES</a>
      <a href="#">CONTACT US</a>
    </nav>
  </div>
</header>

<section class="hero">
  <div class="hero-photo" role="img" aria-label="Night skyline of a city with lit towers by the water"></div>
  <h1 class="hero-title">We bring families<br>together</h1>
  <span class="hero-arrow left"><svg width="8" height="10" viewBox="0 0 8 10"><path d="M6 1 2 5l4 4" fill="none" stroke="#fff" stroke-width="1.8"/></svg></span>
  <span class="hero-arrow right"><svg width="8" height="10" viewBox="0 0 8 10"><path d="M2 1l4 4-4 4" fill="none" stroke="#fff" stroke-width="1.8"/></svg></span>
  <div class="hero-dots"><span class="on"></span><span></span><span></span><span></span><span></span></div>
</section>

<section class="features">
  <div class="container">
    <div class="feature">
      <svg width="24" height="24" viewBox="0 0 24 24"><rect x="5" y="9" width="14" height="11" rx="3" fill="#555"/><rect x="6" y="3" width="3" height="8" rx="1.5" fill="#555"/><rect x="10" y="2" width="3" height="8" rx="1.5" fill="#555"/><rect x="14" y="3" width="3" height="8" rx="1.5" fill="#555"/></svg>
      <p>Your freedom starts with Larkmoor!</p>
    </div>
    <div class="feature">
      <svg width="24" height="24" viewBox="0 0 24 24"><path d="M3 12 12 4l9 8" fill="none" stroke="#555" stroke-width="2"/><path d="M6 11v9h12v-9" fill="none" stroke="#555" stroke-width="2"/><rect x="10" y="14" width="4" height="6" fill="#555"/></svg>
      <p>Larkmoor gets you out</p>
    </div>
    <div class="feature">
      <svg width="24" height="24" viewBox="0 0 24 24"><path d="M12 2 4 5v6c0 5 3.5 9 8 11 4.5-2 8-6 8-11V5z" fill="none" stroke="#555" stroke-width="2"/><circle cx="12" cy="11" r="3" fill="#555"/></svg>
      <p>We guarantee your bail</p>
    </div>
  </div>
</section>

<section class="offer">
  <h2 class="section-title">What we offer</h2>
  <span class="offer-arrow left"><svg width="6" height="8" viewBox="0 0 6 8"><path d="M4.5 1 1.5 4l3 3" fill="none" stroke="#999" stroke-width="1.3"/></svg></span>
  <span class="offer-arrow right"><svg width="6" height="8" viewBox="0 0 6 8"><path d="M1.5 1l3 3-3 3" fill="none" stroke="#999" stroke-width="1.3"/></svg></span>
  <div class="cards">
    <article class="card">
      <div class="card-img drug" role="img" aria-label="Scattered white pills beside a spilled bottle"></div>
      <h3>Drug Charges bails</h3>
      <p>Fast release for drug charge cases</p>
      <a href="#">READ MORE</a>
    </article>
    <article class="card">
      <div class="card-img crime" role="img" aria-label="Close view of an eye with a red tear"></div>
      <h3>Sex Crime bails</h3>
      <p>Discreet help for sex crime cases</p>
      <a href="#">READ MORE</a>
    </article>
    <article class="card">
      <div class="card-img dui" role="img" aria-label="Glass of whiskey next to a set of car keys"></div>
      <h3>DUI bails</h3>
      <p>Quick bail after a DUI arrest</p>
      <a href="#">READ MORE</a>
    </article>
  </div>
</section>

<section class="services">
  <h2 class="section-title">Our services</h2>
  <div class="service-list">
    <div class="service">
      <svg width="28" height="24" viewBox="0 0 28 24"><path d="M8 20v-8a6 6 0 0 1 12 0v8z" fill="none" stroke="#555" stroke-width="2"/><rect x="5" y="20" width="18" height="3" fill="#555"/><line x1="14" y1="1" x2="14" y2="4" stroke="#555" stroke-width="2"/><line x1="4" y1="6" x2="6" y2="8" stroke="#555" stroke-width="2"/><line x1="24" y1="6" x2="22" y2="8" stroke="#555" stroke-width="2"/></svg>
      <h3>Fast</h3>
      <p>We move quickly so your loved one spends less time behind bars.</p>
    </div>
    <div class="service">
      <svg width="28" height="24" viewBox="0 0 28 24"><rect x="3" y="7" width="22" height="15" rx="2" fill="none" stroke="#555" stroke-width="2"/><path d="M10 7V4h8v3" fill="none" stroke="#555" stroke-width="2"/><line x1="3" y1="13" x2="25" y2="13" stroke="#555" stroke-width="2"/></svg>
      <h3>Professional</h3>
      <p>Our licensed agents handle every case with care, respect and full discretion.</p>
    </div>
    <div class="service">
      <svg width="28" height="24" viewBox="0 0 28 24"><path d="M5 8h5a3 3 0 1 1 6 0h5v5a3 3 0 1 1 0 6v3H5z" fill="none" stroke="#555" stroke-width="2"/></svg>
      <h3>Effective</h3>
      <p>We guide your family through each step until the bail is posted.</p>
    </div>
  </div>
</section>

<footer class="site-footer">
  <div class="container">
    <div class="footer-col contact">
      <h4>Contact us</h4>
      <div class="contact-row">
        <p>218 Harlow Avenue, Suite 12<br>Ashford, NY 10452</p>
        <p>Tel: 555-014-2290<br>Fax: 555-014-2291</p>
      </div>
    </div>
    <div class="footer-col newsletter">
      <h4>Newsletter signup</h4>
      <div class="email-field"><span>Enter email</span><b><svg width="6" height="8" viewBox="0 0 6 8"><path d="M1 0l5 4-5 4z" fill="#fff"/></svg></b></div>
    </div>
    <div class="footer-col follow">
      <h4>Follow us on</h4>
      <div class="socials"><span class="social a"></span><span class="social b"></span><span class="social c"></span></div>
    </div>
  </div>
</footer>
<div class="bottom-bar">
  <div class="container">
    <nav><span>HOME</span><span>ABOUT US</span><span>WHAT WE OFFER</span><span>SERVICES</span><span>CONTACT US</span></nav>
    <span>Copyright © 2024 Larkmoor Bails. All Rights Reserved.</span>
  </div>
</div>

</body>
</html>
```